Our brand new and excilting business, ZIPPA things, needs a fresh, vibriant and clean website that is

We need a new website designed to sell our ZIPPA things products to schools and fundraisers. We plan to have around 24 items with great images, add to cart and some really new and cool products. This site needs to be clean, fresh and funky, really clean lines, easy to navigate but look really fun and fresh

Target Market(s)

School fundraising. Kids

Industry/Entity Type

Business

Number of Pages Required

4 page

Colors
add136
fbee3d
fbed22
9bcb3c
f78f20

Requirements
Must have
• Fresh, fun and easy to navigate. Great shopping product page that has images of our products and add to cart
Nice to have
• Flashing image availibility
Should not have
• Must not be old and boring

```html
<!DOCTYPE html>
<html lang="en">
<head>
<meta charset="utf-8">
<title>ZIPPA things – Fundraising Products</title>
<link href="https://fonts.googleapis.com/css2?family=Lato:wght@400;700;900&display=swap" rel="stylesheet">
<style>
:root{
  --green:#9bcb3c;
  --lime:#add136;
  --yellow:#fbee3d;
  --orange:#f78f20;
  --red:#e8402b;
  --ink:#222;
  --muted:#888;
  --line:#e4e4e4;
  --dark:#1b1b1b;
  --darker:#111;
}
*{box-sizing:border-box;margin:0;padding:0}
html,body{width:1200px;height:2364px;overflow:hidden}
body{font-family:'Lato',Arial,sans-serif;color:var(--ink);background:#fff;position:relative}
.wrap{width:824px;margin:0 auto;position:relative}

.topbar{height:30px;background:var(--darker);display:flex;align-items:center;justify-content:space-between;padding:0 12px}
.topbar__note{color:var(--orange);font-size:10px}
.topbar__right{display:flex;align-items:center;gap:8px}
.topbar__cart{background:var(--green);color:#fff;font-size:9px;font-weight:700;padding:3px 10px;border-radius:2px}
.topbar__dot{width:12px;height:12px;background:#444;border-radius:2px}

.header{height:80px;display:flex;align-items:center;justify-content:space-between;padding:0 180px 0 188px}
.brand__name{font-size:30px;font-weight:900;color:var(--green);letter-spacing:-0.5px;line-height:1}
.brand__tag{font-size:9px;color:var(--red);margin-top:3px}
.nav{display:flex;gap:26px;align-items:center;font-size:10px;font-weight:700;color:#333}
.nav a{text-decoration:none;color:inherit}
.nav a.active{color:var(--orange)}

.hero{height:530px;position:relative;background:#050505;overflow:hidden}
.hero__art{position:absolute;left:420px;top:0;width:780px;height:530px;
  background:radial-gradient(circle at 55% 40%,rgba(155,203,60,.55),transparent 35%),
  radial-gradient(circle at 40% 30%,rgba(232,64,43,.5),transparent 30%),
  radial-gradient(circle at 75% 25%,rgba(60,150,230,.55),transparent 30%),
  radial-gradient(circle at 60% 75%,rgba(251,238,61,.45),transparent 30%),
  radial-gradient(circle at 85% 70%,rgba(200,60,200,.4),transparent 30%),#050505}
.hero__text{position:absolute;left:188px;top:112px;width:400px}
.hero__kicker{color:var(--orange);font-weight:900;font-size:26px;letter-spacing:.5px}
.hero__title{color:var(--green);font-weight:900;font-size:66px;line-height:1;margin-top:4px}
.hero__body{color:#ddd;font-size:11px;line-height:1.6;margin-top:18px;width:360px}
.hero__btns{display:flex;gap:12px;margin-top:22px}
.btn{display:inline-block;font-size:10px;font-weight:700;padding:8px 18px;border-radius:2px}
.btn--light{background:#fff;color:#111}
.btn--ghost{border:1px solid #fff;color:#fff}
.hero__arrow{position:absolute;top:250px;width:28px;height:28px;background:rgba(255,255,255,.85);display:flex;align-items:center;justify-content:center}
.hero__arrow--l{left:0}.hero__arrow--r{right:0}
.hero__dots{position:absolute;left:0;right:0;bottom:24px;display:flex;gap:6px;justify-content:center}
.hero__dots span{width:9px;height:9px;border-radius:50%;border:1px solid #fff}
.hero__dots span.on{background:#fff}

.section-title{text-align:center;font-weight:900;font-size:18px;letter-spacing:1px;color:#222}
.section-title::after{content:"";display:block;width:40px;height:2px;background:var(--orange);margin:10px auto 0}

.cards{display:grid;grid-template-columns:repeat(4,184px);gap:29px}
.card__img{height:196px}
.card__body{padding:12px 4px 0}
.card__title{font-size:12px;font-weight:700}
.card__cat{font-size:9px;color:var(--muted);margin-top:3px}
.card__price{font-size:16px;font-weight:900;color:var(--orange);margin-top:5px}
.card__foot{display:flex;justify-content:space-between;align-items:center;margin-top:14px;padding-top:8px;border-top:1px solid var(--line);font-size:9px;color:var(--muted)}
.stars{color:#999;letter-spacing:1px;font-size:10px}
.card--feature{background:#2d3440;padding-bottom:10px}
.card--feature .card__title{color:#fff}
.card--feature .card__cat{color:#bbb}
.card--feature .stars{color:var(--orange)}
.card--feature .card__foot{border-color:#444;color:#ddd}
.card--feature .card__img{position:relative}
.card__badge{position:absolute;left:74px;top:66px;width:36px;height:36px;border-radius:50%;background:var(--orange);display:flex;align-items:center;justify-content:center}

.gallery{position:absolute;left:188px;top:1100px;width:824px;height:460px}
.gallery div{position:absolute}
.gallery__btn{position:absolute;left:170px;top:206px;border:1px solid #fff;color:#fff;font-size:9px;font-weight:700;padding:6px 12px}

.footer{position:absolute;left:0;top:2060px;width:1200px;height:260px;background:var(--dark);color:#ccc}
.footer__col{position:absolute;top:32px}
.footer__col h4{color:#fff;font-size:13px;font-weight:700;margin-bottom:14px}
.footer__col li{list-style:none;font-size:9px;line-height:1.75;color:#aaa}
.footer__input{width:250px;height:28px;background:#fff;margin-bottom:8px}
.footer__sub{width:250px;height:28px;background:var(--orange);color:#fff;font-size:10px;font-weight:700;display:flex;align-items:center;justify-content:center}
.footer__social{display:flex;gap:6px}
.footer__social span{width:20px;height:20px;background:#3d6fb5;display:block}
.copybar{position:absolute;left:0;top:2320px;width:1200px;height:44px;background:var(--darker);color:#888;font-size:9px;display:flex;align-items:center;justify-content:center}
</style>
</head>
<body>

<div class="topbar">
  <span class="topbar__note">Free fast shipping Australia-wide</span>
  <div class="topbar__right"><span class="topbar__cart">MY CART</span><span class="topbar__dot"></span><span class="topbar__dot"></span></div>
</div>

<header class="header">
  <div class="brand">
    <div class="brand__name">ZIPPA things</div>
    <div class="brand__tag">the ultimate fundraising supplier</div>
  </div>
  <nav class="nav">
    <a class="active">HOME</a><a>ABOUT US</a><a>PRODUCTS</a><a>GLOW STICKS</a><a>PARTY SUPPLIES</a><a>CONTACT US</a>
    <svg width="12" height="12" viewBox="0 0 12 12"><circle cx="5" cy="5" r="3.8" fill="none" stroke="#f78f20" stroke-width="1.6"/><line x1="8" y1="8" x2="11" y2="11" stroke="#f78f20" stroke-width="1.6"/></svg>
  </nav>
</header>

<section class="hero">
  <div class="hero__art" role="img" aria-label="Bright coloured paint splashing from glowing jars on a black background"></div>
  <div class="hero__text">
    <div class="hero__kicker">SPECIAL DISCOUNT</div>
    <div class="hero__title">LOREM IPSUM</div>
    <p class="hero__body">Bright glow products for every school fundraiser and party night. Order in bulk, share with friends and light up your next event with fun colours that last all night.</p>
    <div class="hero__btns"><span class="btn btn--light">MORE DETAIL</span><span class="btn btn--ghost">SHOP NOW</span></div>
  </div>
  <div class="hero__arrow hero__arrow--l"><svg width="10" height="10"><path d="M7 1 3 5l4 4" fill="none" stroke="#333" stroke-width="2"/></svg></div>
  <div class="hero__arrow hero__arrow--r"><svg width="10" height="10"><path d="M3 1l4 4-4 4" fill="none" stroke="#333" stroke-width="2"/></svg></div>
  <div class="hero__dots"><span class="on"></span><span></span><span></span><span></span></div>
</section>

<h2 class="section-title" style="position:absolute;left:0;right:0;top:694px">FEATURED ITEMS</h2>
<div class="wrap" style="position:absolute;left:188px;top:750px">
  <div class="cards">
    <article class="card"><div class="card__img" role="img" aria-label="Rainbow glow sticks" style="background:linear-gradient(135deg,#111,#2a1a3a 50%,#111)"></div>
      <div class="card__body"><div class="card__title">Product Title Here</div><div class="card__cat">Glow sticks</div><div class="card__price">$199</div><div class="card__foot"><span class="stars">★★★★★</span><span>Add to Cart</span></div></div></article>
    <article class="card"><div class="card__img" role="img" aria-label="Green glow glasses" style="background:radial-gradient(circle,#4a7a1a,#111 65%)"></div>
      <div class="card__body"><div class="card__title">Product Title Here</div><div class="card__cat">Glow glasses</div><div class="card__price">$125</div><div class="card__foot"><span class="stars">★★★★★</span><span>Add to Cart</span></div></div></article>
    <article class="card"><div class="card__img" role="img" aria-label="Glowing party cups" style="background:radial-gradient(circle,#6a7a1a,#111 65%)"></div>
      <div class="card__body"><div class="card__title">Product Title Here</div><div class="card__cat">Glow cups</div><div class="card__price">$238</div><div class="card__foot"><span class="stars">★★★★★</span><span>Add to Cart</span></div></div></article>
    <article class="card"><div class="card__img" role="img" aria-label="Glowing cocktail glasses" style="background:radial-gradient(circle,#6a2a6a,#111 65%)"></div>
      <div class="card__body"><div class="card__title">Product Title Here</div><div class="card__cat">Glow glasses</div><div class="card__price">$299</div><div class="card__foot"><span class="stars">★★★★★</span><span>Add to Cart</span></div></div></article>
  </div>
</div>

<div class="gallery">
  <div role="img" aria-label="Glow stick bundle close up" style="left:0;top:0;width:200px;height:256px;background:linear-gradient(160deg,#555,#222)"></div>
  <div role="img" aria-label="Crowd at a glow party" style="left:204px;top:0;width:204px;height:256px;background:linear-gradient(160deg,#2a2a5a,#7a3a8a)"></div>
  <div role="img" aria-label="Glowing balloons" style="left:0;top:260px;width:408px;height:200px;background:radial-gradient(circle at 50% 50%,#c8d84a,#6a3a8a 60%,#222)"></div>
  <div role="img" aria-label="Green light painting in the dark" style="left:416px;top:0;width:408px;height:460px;background:radial-gradient(circle at 50% 55%,#3fc87a,#0a2a1a 55%,#050505)"><span class="gallery__btn">SHOP NOW</span></div>
</div>

<h2 class="section-title" style="position:absolute;left:0;right:0;top:1626px">RECENT ITEMS</h2>
<div class="wrap" style="position:absolute;left:188px;top:1682px">
  <div class="cards">
    <article class="card"><div class="card__img" role="img" aria-label="Child wearing glow necklaces" style="background:linear-gradient(160deg,#3a2a2a,#111)"></div>
      <div class="card__body"><div class="card__title">Product Title Here</div><div class="card__cat">Glow necklaces</div><div class="card__price">$199</div><div class="card__foot"><span class="stars">★★★★★</span><span>Add to Cart</span></div></div></article>
    <article class="card card--feature"><div class="card__img" role="img" aria-label="Glowing bracelets" style="background:linear-gradient(160deg,#3a4a6a,#222)"><span class="card__badge"><svg width="14" height="14"><path d="M7 2v10M2 7h10" stroke="#fff" stroke-width="2"/></svg></span></div>
      <div class="card__body"><div class="card__title">Product Title Here</div><div class="card__cat">Glow bracelets</div><div class="card__price">$125</div><div class="card__foot"><span class="stars">★★★★★</span><span>Add to Cart</span></div></div></article>
    <article class="card"><div class="card__img" role="img" aria-label="Tube of glow sticks" style="background:linear-gradient(160deg,#1a3a1a,#111)"></div>
      <div class="card__body"><div class="card__title">Product Title Here</div><div class="card__cat">Glow sticks</div><div class="card__price">$238</div><div class="card__foot"><span class="stars">★★★★★</span><span>Add to Cart</span></div></div></article>
    <article class="card"><div class="card__img" role="img" aria-label="Coloured glow rings" style="background:radial-gradient(circle,#3a6aa8,#111 65%)"></div>
      <div class="card__body"><div class="card__title">Product Title Here</div><div class="card__cat">Glow rings</div><div class="card__price">$299</div><div class="card__foot"><span class="stars">★★★★★</span><span>Add to Cart</span></div></div></article>
  </div>
</div>

<footer class="footer">
  <div class="footer__col" style="left:188px"><h4>Shopping with us</h4><ul><li>Why shop with us</li><li>How to order</li><li>Delivery</li><li>Returns</li><li>Secure payment</li><li>Gift cards</li><li>Bulk deals</li><li>FAQ</li></ul></div>
  <div class="footer__col" style="left:380px"><h4>About us</h4><ul><li>Our story</li><li>Fundraisers</li><li>Schools</li><li>Community</li><li>Meet the team</li><li>Careers</li><li>Privacy policy</li></ul></div>
  <div class="footer__col" style="left:548px"><h4>Selling with us</h4><ul><li>Wholesale</li><li>Stores</li><li>Become a partner</li><li>Affiliates</li></ul></div>
  <div class="footer__col" style="left:748px"><h4>Signup newsletter</h4><div class="footer__input"></div><div class="footer__sub">SUBSCRIBE NOW</div>
    <h4 style="margin-top:18px">Keep in touch</h4><div class="footer__social"><span></span><span style="background:#4aa3df"></span><span style="background:#c94a3a"></span><span style="background:#2b5f8a"></span></div></div>
</footer>
<div class="copybar">Copyright © 2016 ZIPPA things. All rights reserved.</div>

</body>
</html>
```